依頼概要
■依頼の目的/概要
食と歯のプロがタッグを組んでチーズの虫歯予防効果(チーズは虫歯予防の最強食品だった)を一緒に学ぶ、というコンセプトで出版する電子書籍の表紙デザインをお願いします。

■本の内容
歯と食の専門家に向けてチーズの虫歯予防効果に関する情報を共有する書籍です。

■デザイン要望
1. タイトルの要素:①この書籍は誰向けか(対象)、②読むと何を得られるのか、③書いた私は誰か、これら3点が明確に伝わるよう表現ください。

2. 上の具体例は、次のようになります。
①歯と食のプロがタッグを組もう!→この本の対象は「栄養士と歯科医」
②チーズの虫歯予防効果を学ぶ本→チーズの虫歯予防効果がわかる
③歯科医師・森川修平*ブライトリーフ口腔保健総合研究所→著者は歯の専門家

2. 書籍タイトルの調整:タイトルは検討中ですが、原稿の最初にあるような例を想定して書体等を含めデザインください。コンペの採択後、確定したタイトルを落とし込んで納品をお願いします。

3. 添付ファイル(書籍内容)は著者の知的財産なので守秘願います。

4. その他何かご不明な点がございましたら、お気軽にご質問下さい。

よろしくお願いいたします。
追記
1. 出版先:電子出版はBorvexaのルミナを予定しています。
2. 調整および納品:コンペでデザインを採択後、最終的に、
①標題等テキストの確定に伴う字句の修正、および
②画像に関する調整の完了・データ引き渡し、
これらをもって納品と致します。
■ 選んだ理由

タイトルの視認性がルミナショップの標準サイズで明瞭に読めるサイズである点、また、そのツカミから導入される帯部分に情報が多く、総じて「表紙」自体を読んでみたい、というモチベーションを高める工夫が秀逸でした。また、帯のキャッチについても多数ご提案を頂き、著者として大変参考となり当選とさせて頂きました。

■ 提案者全員のお礼・コメント

ジョブラーの皆様

著者の森川です。

このたびは私共の電子書籍について表紙デザインのご提案を多数賜り、本当にありがとうございました。

お寄せ頂いたいずれの作品もオリジナリティに溢れ、創意工夫のご努力に対し関係者一同、深く敬意を表します。

これまで出版は内容一本で勝負してきましたが、今回の依頼を通じ「表紙は書籍の顔」というコンセプトを明確に自覚でき、著者として大変勉強になりました。あらためて皆様に厚く御礼申し上げます。

次の出版も計画中ですので、皆様には今後ともご支援のほど何卒宜しくお願い申し上げます。

```html
<!DOCTYPE html>
<html lang="ja">
<head>
<meta charset="utf-8">
<title>チーズは虫歯予防の最強食品だった</title>
<link rel="stylesheet" href="https://fonts.googleapis.com/css2?family=Noto+Serif+JP:wght@700;900&family=Noto+Sans+JP:wght@500;700&display=swap">
<style>
  :root {
    --paper: #ffffff;
    --ink: #1a1a1a;
    --red: #c8161d;
    --band-text: #ffffff;
    --tooth: #dbeaf5;
    --cheese: #f3c94a;
  }
  * { margin: 0; padding: 0; box-sizing: border-box; }
  html, body { width: 749px; height: 1200px; overflow: hidden; background: var(--paper); }
  .cover {
    position: relative;
    width: 749px;
    height: 1200px;
    background: var(--paper);
    overflow: hidden;
    font-family: "Noto Serif JP", serif;
  }
  .title-col {
    position: absolute;
    writing-mode: vertical-rl;
    font-weight: 900;
    line-height: 1;
    letter-spacing: -0.02em;
    white-space: nowrap;
  }
  .kicker { right: 26px; top: 22px; font-size: 66px; color: var(--ink); }
  .title-cheese { right: 140px; top: 55px; font-size: 132px; color: var(--red); }
  .title-cavity { right: 292px; top: 28px; font-size: 166px; color: var(--ink); }
  .title-best { right: 480px; top: 45px; font-size: 140px; color: var(--red); }
  .small { font-size: 0.55em; }
  .band {
    position: absolute;
    left: 0; right: 0; bottom: 0;
    height: 313px;
    background: var(--red);
  }
  .characters {
    position: absolute;
    left: 140px;
    top: 838px;
    width: 500px;
    height: 180px;
  }
  .institute {
    position: absolute;
    right: 34px;
    bottom: 148px;
    font-family: "Noto Sans JP", sans-serif;
    font-weight: 500;
    font-size: 21px;
    color: var(--band-text);
  }
  .author {
    position: absolute;
    left: 30px;
    right: 30px;
    bottom: 62px;
    display: flex;
    align-items: baseline;
    color: var(--band-text);
    font-family: "Noto Sans JP", sans-serif;
    font-weight: 700;
  }
  .author-label { font-size: 34px; margin-right: 22px; }
  .author-role { font-size: 22px; margin-right: 14px; }
  .author-name { font-family: "Noto Serif JP", serif; font-weight: 900; font-size: 52px; letter-spacing: 0.06em; }
</style>
</head>
<body>
<div class="cover">
  <div class="title-col kicker">歯と食のプロ必見！</div>
  <div class="title-col title-cheese">チーズ<span class="small">は</span></div>
  <div class="title-col title-cavity">虫歯予防<span class="small">の</span></div>
  <div class="title-col title-best">最強食品<span class="small">だった</span></div>

  <div class="band"></div>

  <svg class="characters" viewBox="0 0 500 180" role="img" aria-label="寄り添う歯とチーズのキャラクターのイラスト">
    <defs>
      <linearGradient id="tone" x1="0" y1="0" x2="1" y2="0">
        <stop offset="0" stop-color="#dbeaf5"/>
        <stop offset="1" stop-color="#f3c94a"/>
      </linearGradient>
    </defs>
    <rect x="0" y="0" width="500" height="180" rx="40" fill="url(#tone)"/>
  </svg>

  <div class="institute">ブライトリーフ口腔保健総合研究所</div>
  <div class="author">
    <span class="author-label">著者</span>
    <span class="author-role">歯科医師</span>
    <span class="author-name">森川 修平</span>
  </div>
</div>
</body>
</html>
```